Small Accounting Practice needs something creative

We need a business card design for a new small accounting practice based in Perth, Australia. The name of the practice is 'Kowra Ledger Partners Pty Ltd'. We providing Tax, Bookkeeping and Accounting services. Our target are individuals and small businesses. We want the design to be simply and creative. Also, we can the design can help us to gain people's trust.

Target Market(s)

Individuals and small businesses.

Industry/Entity Type

Accounting

Colors

Designer to choose colors to be used in the design.

```html
<!DOCTYPE html>
<html lang="en">
<head>
<meta charset="utf-8">
<title>Kowra Ledger Partners – Business Card</title>
<link rel="stylesheet" href="https://fonts.googleapis.com/css2?family=Roboto+Condensed:wght@300;400;700&display=swap">
<style>
  :root {
    --stage: #030306;
    --card-dark: #505152;
    --band-dark: #4d4e4f;
    --card-light: #f4f6f5;
    --label: #f2f2f2;
    --name-light: #ffffff;
    --services: #6d6e6f;
    --ink: #444546;
    --ink-strong: #3b3c3d;
    --accent-blue: #6cc7ec;
    --accent-orange: #f5a623;
  }
  * { margin: 0; padding: 0; box-sizing: border-box; }
  html, body {
    width: 1200px;
    height: 1200px;
    overflow: hidden;
    background: var(--stage);
  }
  .canvas {
    position: relative;
    width: 1200px;
    height: 1200px;
    font-family: "Roboto Condensed", "Arial Narrow", sans-serif;
  }
  .panel-label {
    position: absolute;
    left: 0;
    width: 1200px;
    text-align: center;
    color: var(--label);
    font-weight: 300;
    font-size: 24px;
    letter-spacing: 0.5px;
  }
  .panel-label--front { top: 97px; }
  .panel-label--back { top: 673px; }

  /* Front of card */
  .card-front {
    position: absolute;
    left: 314px;
    top: 174px;
    width: 567px;
    height: 322px;
    background: var(--card-dark);
  }
  .card-front__brand {
    position: absolute;
    left: 0;
    top: 140px;
    width: 567px;
    display: flex;
    justify-content: center;
    align-items: center;
    gap: 14px;
    transform: translateY(-50%);
  }
  .card-front__mark {
    width: 26px;
    height: 26px;
    background: var(--accent-orange);
    flex: none;
  }
  .card-front__name {
    color: var(--name-light);
    font-weight: 400;
    font-size: 38px;
    letter-spacing: -0.2px;
    white-space: nowrap;
  }
  .card-front__services {
    position: absolute;
    left: 0;
    top: 280px;
    width: 567px;
    text-align: center;
    color: var(--services);
    font-weight: 700;
    font-size: 29px;
    letter-spacing: 0.3px;
    white-space: pre;
  }

  /* Back of card */
  .card-back {
    position: absolute;
    left: 314px;
    top: 744px;
    width: 569px;
    height: 323px;
    background: var(--card-light);
    overflow: hidden;
  }
  .card-back__band {
    position: absolute;
    left: 0;
    top: 0;
    width: 56px;
    height: 323px;
    background: var(--band-dark);
  }
  .card-back__mark {
    position: absolute;
    left: 40px;
    top: 40px;
    width: 16px;
    height: 16px;
    background: var(--accent-blue);
  }
  .card-back__contact {
    position: absolute;
    left: 84px;
    top: 61px;
  }
  .contact__name {
    color: var(--ink-strong);
    font-weight: 700;
    font-size: 20px;
    line-height: 24px;
  }
  .contact__role {
    color: var(--ink);
    font-weight: 400;
    font-size: 20px;
    line-height: 30px;
  }
  .contact__email {
    color: var(--accent-blue);
    font-weight: 400;
    font-size: 20px;
    line-height: 30px;
  }
  .card-back__registration {
    position: absolute;
    right: 21px;
    bottom: 8px;
    color: var(--ink);
    font-weight: 400;
    font-size: 17px;
  }
</style>
</head>
<body>
  <main class="canvas">
    <p class="panel-label panel-label--front">FRONT PANEL</p>

    <section class="card-front" aria-label="Business card front">
      <div class="card-front__brand">
        <span class="card-front__mark"></span>
        <span class="card-front__name">Kowra Ledger Partners Pty Ltd</span>
      </div>
      <p class="card-front__services">TAX   |  BOOKKEEPING  |  ACCOUNTING</p>
    </section>

    <p class="panel-label panel-label--back">BACK PANEL</p>

    <section class="card-back" aria-label="Business card back">
      <div class="card-back__band"></div>
      <div class="card-back__mark"></div>
      <div class="card-back__contact">
        <p class="contact__name">Daniel Oakes</p>
        <p class="contact__role">Accountant &amp; Small Business Consultant</p>
        <p class="contact__email">daniel@kowraledger.com.au</p>
      </div>
      <p class="card-back__registration">Registered ASIC Agent 40817</p>
    </section>
  </main>
</body>
</html>
```